Pelin Thai Massage Double Sided Flyer Luxury

I require a double sided flyer
we are a Thai Massage Spa
Would like gold, deep purple and bronze colours
Something eye catching and looks professional

```html
<!DOCTYPE html>
<html lang="en">
<head>
<meta charset="utf-8">
<title>Pelin Thai Massage – Double Sided Flyer</title>
<link rel="stylesheet" href="https://fonts.googleapis.com/css2?family=Lato:wght@400;700&family=Kaushan+Script&family=Lobster+Two:ital,wght@1,700&family=Titan+One&display=swap">
<style>
:root{
  --stage:#333333;
  --purple:#7e3f98;
  --purple-deep:#5f2a78;
  --purple-soft:#8d4da6;
  --gold:#f5c242;
  --gold-deep:#e8a92a;
  --white:#ffffff;
  --ink:#1b1b1b;
}
*{box-sizing:border-box;margin:0;padding:0}
html,body{width:1200px;height:1200px;overflow:hidden;background:var(--stage)}
body{position:relative;font-family:"Lato",sans-serif;color:var(--white)}
.flyer{position:absolute;top:246px;overflow:hidden;background:#f1f1f1;box-shadow:0 6px 18px rgba(0,0,0,.45)}
.flyer--front{left:74px;width:508px;height:714px}
.flyer--back{left:612px;width:511px;height:716px}
.photo{position:absolute}
.shape{position:absolute;left:0;top:0}
.abs{position:absolute}

/* front */
.photo--massage{left:0;top:0;width:508px;height:340px;background:linear-gradient(115deg,#5a3419 0%,#a4632f 35%,#d9b08a 60%,#efe3d4 85%,#f6efe6 100%)}
.photo--stones{left:360px;top:440px;width:148px;height:240px;background:linear-gradient(180deg,#e9ecea 0%,#8d928a 35%,#5c6359 65%,#dfe2de 100%)}
.brand{left:28px;top:86px;display:flex;align-items:center;gap:6px;font-size:15px;color:var(--gold);letter-spacing:.2px}
.brand__dot{width:10px;height:10px;border-radius:50%;background:var(--gold)}
.welcome{left:28px;top:360px;font-family:"Kaushan Script",cursive;font-size:40px;color:var(--gold);line-height:1}
.lead{left:22px;width:430px;font-size:11.6px;line-height:14px}
.lead--one{top:420px}
.lead--two{top:454px;width:400px}
.subhead{left:22px;font-size:13px;color:var(--gold)}
.subhead--forms{top:514px}
.subhead--benefits{top:577px;left:24px}
.check{display:flex;align-items:center;gap:10px;font-size:12px;top:541px}
.check--oil{left:28px}
.check--floor{left:206px}
.benefits{left:34px;top:604px;list-style:none;font-size:11px;line-height:20px}
.benefits li{display:flex;align-items:center;gap:12px}
.benefits li::before{content:"";width:8px;height:8px;border-radius:50%;background:var(--gold)}
.open{font-family:"Lobster Two",cursive;font-style:italic;font-weight:700;font-size:15px;color:var(--ink)}
.open--front{left:371px;top:676px}
.badge{position:absolute;width:98px;height:98px;border-radius:50%;background:var(--white);border:4px solid var(--gold);display:flex;align-items:center;justify-content:center;text-align:center;font-family:"Lobster Two",cursive;font-style:italic;font-weight:700;font-size:14px;line-height:17px;color:var(--purple)}
.badge--front{left:349px;top:292px}
.badge--back{left:50px;top:326px}
.contact{display:flex;align-items:center;gap:10px;font-size:6.8px;line-height:8px}
.contact--front{left:22px;top:693px}
.contact--back{left:198px;top:694px}
.contact__item{display:flex;align-items:center;gap:3px}
.contact__item svg{width:8px;height:8px;flex:none}

/* back */
.photo--strip-a{left:0;top:0;width:46px;height:340px;background:linear-gradient(180deg,#c88a50,#e7b47e 50%,#caa377)}
.photo--candles{left:50px;top:0;width:182px;height:150px;background:linear-gradient(135deg,#3a6a1c,#5e9c2b 45%,#3b2416 80%)}
.photo--shoulder{left:240px;top:0;width:271px;height:150px;background:linear-gradient(110deg,#f3e6da,#d9a27a 40%,#a8653c 70%,#2a1b14)}
.photo--face{left:52px;top:158px;width:370px;height:200px;background:linear-gradient(120deg,#1f4a10,#4f8f22 40%,#7fbf3a 60%,#d9a27c 85%)}
.photo--leaf{left:427px;top:158px;width:84px;height:132px;background:linear-gradient(150deg,#6fb12d,#3d7a1a)}
.photo--strip-b{left:0;top:350px;width:80px;height:122px;background:linear-gradient(180deg,#4a7a22,#e8e6e0 60%,#6b5a3f)}
.photo--hands{left:0;top:480px;width:200px;height:236px;background:linear-gradient(150deg,#d29b72,#f0cfb3 50%,#e9dfd7)}
.title{left:0;width:511px;text-align:center;top:378px;padding-left:94px;font-family:"Titan One",sans-serif;font-size:28px;color:var(--gold);transform:skewX(-10deg);letter-spacing:.5px}
.intro{left:128px;top:428px;width:370px;text-align:center;font-size:11.6px;line-height:14px}
.menu{left:168px;width:320px;text-align:center}
.menu__name{font-family:"Titan One",sans-serif;font-size:15px;transform:skewX(-10deg);letter-spacing:.3px}
.menu__price{font-weight:700;font-size:11.5px;line-height:14px}
.menu__desc{font-size:11.5px;line-height:14px}
.menu--deep{top:476px}
.menu--deep-90{top:537px}
.menu--floor{top:584px;left:148px;width:360px}
.pill{left:257px;top:664px;padding:1px 8px;border-radius:10px;background:var(--gold)}
</style>
</head>
<body>

<!-- FRONT -->
<section class="flyer flyer--front">
  <div class="photo photo--massage" role="img" aria-label="Photo of a woman relaxing on a towel receiving a back massage beside a lit candle"></div>
  <div class="photo photo--stones" role="img" aria-label="Photo of a stack of grey hot massage stones"></div>
  <svg class="shape" width="508" height="714" viewBox="0 0 508 714" aria-hidden="true">
    <path class="accent-band" d="M300 334 C360 318 420 312 458 290 C480 277 498 256 508 224 L508 278 C496 300 484 312 466 322 C430 330 360 334 300 334 Z" fill="var(--gold)"/>
    <path d="M0 232 C110 320 260 336 390 318 C450 310 478 330 476 378 C470 470 420 560 330 714 L0 714 Z" fill="var(--purple)"/>
    <path d="M0 232 C110 320 260 336 390 318 C430 312 450 322 462 340 C420 332 360 345 300 345 C170 345 70 300 0 252 Z" fill="var(--purple-deep)" opacity=".55"/>
    <path d="M476 378 C470 470 420 560 330 714 L346 714 C430 570 486 470 488 380 Z" fill="var(--purple-deep)"/>
  </svg>

  <div class="abs brand"><span class="brand__dot"></span>Pelin Thai Massage</div>
  <div class="badge badge--front">Gift Vouchers<br>Available</div>

  <h1 class="abs welcome">Welcome to Luxury</h1>
  <p class="abs lead lead--one">Set in the heart of Roundhay, Pelin Thai Massage will allow you to immerse yourself in a place where your wellbeing and rejuvenation is at the centre of what we do.</p>
  <p class="abs lead lead--two">Using Thai traditions, our highly trained therapists offer revitalising body treatments with their deep tissue massage techniques. In their hands, you will see and feel immediate results.</p>

  <h2 class="abs subhead subhead--forms">We offer two forms of massages :</h2>
  <div class="abs check check--oil"><svg width="16" height="14" viewBox="0 0 16 14"><rect x="1" y="3" width="10" height="10" fill="none" stroke="var(--gold)" stroke-width="1.6"/><path d="M3 7 L6 10 L15 1" fill="none" stroke="var(--gold)" stroke-width="2.4"/></svg>Traditional Oil Massage</div>
  <div class="abs check check--floor"><svg width="16" height="14" viewBox="0 0 16 14"><rect x="1" y="3" width="10" height="10" fill="none" stroke="var(--gold)" stroke-width="1.6"/><path d="M3 7 L6 10 L15 1" fill="none" stroke="var(--gold)" stroke-width="2.4"/></svg>Traditional Floor Massage</div>

  <h2 class="abs subhead subhead--benefits">Benefits of full body massage include :</h2>
  <ul class="abs benefits">
    <li>Relief from general muscular aches and pains</li>
    <li>Improve circulation and stimulate the lymphatic system</li>
    <li>Alleviation of physical and emotional tension</li>
    <li>Release and relaxation of muscles and improve flexibility</li>
  </ul>

  <div class="abs open open--front">Open 7 Days a Week</div>

  <div class="abs contact contact--front">
    <span class="contact__item"><svg viewBox="0 0 8 8"><path d="M4 0 A3 3 0 0 1 7 3 C7 5 4 8 4 8 C4 8 1 5 1 3 A3 3 0 0 1 4 0 Z" fill="#fff"/><circle cx="4" cy="3" r="1.1" fill="var(--purple)"/></svg><span>Pelin Thai Massage<br>14 Oakfield Road, Leeds, LS8 2QT</span></span>
    <span class="contact__item"><svg viewBox="0 0 8 8"><circle cx="4" cy="4" r="3.5" fill="none" stroke="#fff" stroke-width=".8"/><path d="M2.6 2.3 L3.4 2.1 L3.8 3.2 L3.3 3.6 C3.6 4.3 4 4.7 4.5 4.9 L4.9 4.4 L5.9 4.8 L5.7 5.6 C4 5.8 2.4 4.1 2.6 2.3 Z" fill="#fff"/></svg>0113 496 0720</span>
    <span class="contact__item"><svg viewBox="0 0 8 8"><circle cx="4" cy="4" r="3.4" fill="none" stroke="#fff" stroke-width=".8"/><path d="M.6 4 H7.4 M4 .6 C2.4 2.5 2.4 5.5 4 7.4 M4 .6 C5.6 2.5 5.6 5.5 4 7.4" fill="none" stroke="#fff" stroke-width=".6"/></svg>www.pelinthaimassage.co.uk</span>
  </div>
</section>

<!-- BACK -->
<section class="flyer flyer--back">
  <div class="photo photo--strip-a" role="img" aria-label="Photo detail of warm skin tones"></div>
  <div class="photo photo--candles" role="img" aria-label="Photo of lit spa candles on dark wood with green leaves"></div>
  <div class="photo photo--shoulder" role="img" aria-label="Photo of hands massaging a woman's shoulders"></div>
  <div class="photo photo--face" role="img" aria-label="Photo of a woman receiving a relaxing facial massage among green leaves"></div>
  <div class="photo photo--leaf" role="img" aria-label="Photo of a green potted plant"></div>
  <div class="photo photo--strip-b" role="img" aria-label="Photo of spa stones and leaves"></div>
  <div class="photo photo--hands" role="img" aria-label="Photo of hands giving a back massage"></div>
  <svg class="shape" width="511" height="716" viewBox="0 0 511 716" aria-hidden="true">
    <path d="M80 348 C220 345 400 320 511 264 L511 716 L196 716 C150 610 110 480 80 348 Z" fill="var(--purple)"/>
    <path d="M80 348 C110 480 150 610 196 716 L184 716 C140 610 96 480 66 352 Z" fill="var(--purple-deep)"/>
    <path d="M80 348 C220 345 400 320 511 264 L511 280 C400 335 230 360 84 362 Z" fill="var(--purple-soft)" opacity=".6"/>
  </svg>

  <div class="badge badge--back">Gift Vouchers<br>Available</div>

  <h1 class="abs title">MASSAGES</h1>
  <p class="abs intro">Restore balance. Revive your senses. Discover all the ways Pelin Thai Massage can breathe new life into your body and soul.</p>

  <div class="abs menu menu--deep">
    <h2 class="menu__name">DEEP TISSUE MASSAGE</h2>
    <p class="menu__price">60 minutes £45</p>
    <p class="menu__desc">Oil massage personalised, light to firm pressure</p>
  </div>
  <div class="abs menu menu--deep-90">
    <p class="menu__price">90 minutes £55</p>
    <p class="menu__desc">Oil massage, medium to firm pressure</p>
  </div>
  <div class="abs menu menu--floor">
    <h2 class="menu__name">THAI FLOOR TRADTIONAL MASSAGE</h2>
    <p class="menu__price">60 minutes £45</p>
    <p class="menu__desc">Dry massage, medium to firm pressure applying<br>stretching technique</p>
  </div>

  <div class="abs pill open">Open 7 Days a Week</div>

  <div class="abs contact contact--back">
    <span class="contact__item"><svg viewBox="0 0 8 8"><path d="M4 0 A3 3 0 0 1 7 3 C7 5 4 8 4 8 C4 8 1 5 1 3 A3 3 0 0 1 4 0 Z" fill="#fff"/><circle cx="4" cy="3" r="1.1" fill="var(--purple)"/></svg><span>Pelin Thai Massage<br>14 Oakfield Road, Leeds, LS8 2QT</span></span>
    <span class="contact__item"><svg viewBox="0 0 8 8"><circle cx="4" cy="4" r="3.5" fill="none" stroke="#fff" stroke-width=".8"/><path d="M2.6 2.3 L3.4 2.1 L3.8 3.2 L3.3 3.6 C3.6 4.3 4 4.7 4.5 4.9 L4.9 4.4 L5.9 4.8 L5.7 5.6 C4 5.8 2.4 4.1 2.6 2.3 Z" fill="#fff"/></svg>0113 496 0720</span>
    <span class="contact__item"><svg viewBox="0 0 8 8"><circle cx="4" cy="4" r="3.4" fill="none" stroke="#fff" stroke-width=".8"/><path d="M.6 4 H7.4 M4 .6 C2.4 2.5 2.4 5.5 4 7.4 M4 .6 C5.6 2.5 5.6 5.5 4 7.4" fill="none" stroke="#fff" stroke-width=".6"/></svg>www.pelinthaimassage.co.uk</span>
  </div>
</section>

</body>
</html>
```